WWW.VELTRONA.IT BUSINNES CARD

WE NEED A BUSINESS CARD . I HAVE A COMPANY IN ITALY NR 1 IN HAIR MEDICAL CARE AN HAIR REPLECEMENT . IN CARD I NEED WRITE WEB ADDRESS, MAIL , ADDRESS, TELEPHONE NUMBER , AND NAME
IN THE BACK SIDE I NEED MY DOCTOR LOGO .
MY WEB SITE IS WWW.VELTRONA.IT
Updates

Target Market(s)

CONSUMER B2C

Industry/Entity Type

Hair And Beauty

Contact Information for Business Card

I WANT A MEDICAL BUSINESS CARD.

Font styles to use
Other font styles liked:
• VERDANA

Colors
33a6d7
3176b5
85abd2
aedbee
eaf1f7
ffffff

Requirements
Must have
• I NEED MY LOGO AND LOGO OF DR VELTRONA

```html
<!DOCTYPE html>
<html lang="it">
<head>
<meta charset="utf-8">
<title>Veltrona – Business Card</title>
<link href="https://fonts.googleapis.com/css2?family=Work+Sans:wght@400;500;600&display=swap" rel="stylesheet">
<style>
  :root {
    --stage: #2b2b2d;
    --card-blue: #0b5597;
    --brand-blue: #1261a8;
    --sky: #33a6d7;
    --paper: #f4f5f6;
    --white: #ffffff;
    --mascot-brown: #8a4a24;
    --mascot-skin: #efb48e;
  }
  * { margin: 0; padding: 0; box-sizing: border-box; }
  html, body { width: 1200px; height: 930px; overflow: hidden; }
  body {
    background: var(--stage);
    font-family: "Work Sans", Verdana, sans-serif;
    position: relative;
  }

  /* Back side */
  .card-back {
    position: absolute;
    left: 85px; top: 148px;
    width: 363px; height: 634px;
    background: var(--card-blue);
    overflow: hidden;
  }
  .mascot-area {
    position: absolute;
    left: 47px; top: 58px;
    width: 268px; height: 520px;
    border-radius: 40% 40% 50% 50% / 20% 20% 12% 12%;
    background: linear-gradient(180deg, rgba(138,74,36,0.55) 0%, rgba(138,74,36,0.7) 60%, rgba(239,180,142,0.75) 100%);
  }
  .doctor-name {
    position: absolute;
    left: 272px; top: 408px;
    transform: translate(-50%, -50%) rotate(-90deg);
    white-space: nowrap;
    color: var(--white);
    font-weight: 500;
    font-size: 32px;
    letter-spacing: 0.5px;
  }

  /* Front side */
  .card-front {
    position: absolute;
    left: 482px; top: 418px;
    width: 633px; height: 364px;
    background: var(--paper);
    overflow: hidden;
  }
  .card-front .wave { position: absolute; left: 0; top: 0; }
  .brand {
    position: absolute;
    left: 356px; top: 66px;
    display: flex; align-items: center; gap: 10px;
  }
  .brand-mark {
    width: 30px; height: 30px;
    background: var(--sky);
  }
  .brand-name {
    color: var(--brand-blue);
    font-weight: 600;
    font-size: 40px;
    line-height: 1;
  }
  .brand-tagline {
    position: absolute;
    left: 359px; top: 117px;
    color: var(--brand-blue);
    font-size: 11px;
    letter-spacing: 0.2px;
  }
  .holder {
    position: absolute;
    left: 35px; top: 212px;
    color: var(--white);
  }
  .holder-name { font-size: 23px; font-weight: 500; line-height: 1.1; }
  .holder-role { font-size: 16px; margin-top: 2px; }
  .contacts {
    position: absolute;
    left: 35px; top: 275px;
    list-style: none;
    color: var(--white);
    font-size: 17px;
    line-height: 21px;
  }
  .contacts li { display: flex; align-items: center; gap: 7px; }
  .contacts svg { width: 10px; height: 10px; flex: none; }
  .address {
    position: absolute;
    right: 38px; top: 296px;
    text-align: right;
    color: var(--white);
    font-size: 17px;
    line-height: 21px;
    font-style: normal;
  }
</style>
</head>
<body>

<section class="card-back">
  <div class="mascot-area" role="img" aria-label="Cartoon mascot: a smiling hair strand doctor in a white coat giving a thumbs up, standing on a round peach base"></div>
  <div class="doctor-name">dr. Veltrona</div>
</section>

<section class="card-front">
  <svg class="wave" width="633" height="364" viewBox="0 0 633 364">
    <path d="M0 188 C120 158 240 185 330 210 C420 235 520 225 633 160 L633 364 L0 364 Z" fill="var(--card-blue)"/>
    <path d="M0 186 C120 156 240 183 330 208 C420 233 520 223 633 158" fill="none" stroke="var(--sky)" stroke-width="5"/>
    <path d="M343 150 C420 140 470 156 520 155 C560 154 590 146 630 138" fill="none" stroke="var(--sky)" stroke-width="2.5"/>
  </svg>

  <div class="brand">
    <span class="brand-mark"></span>
    <span class="brand-name">Veltrona</span>
  </div>
  <div class="brand-tagline">CURA E REINTEGRAZIONE DEI CAPELLI</div>

  <div class="holder">
    <div class="holder-name">MARCO BELLINI</div>
    <div class="holder-role">Director</div>
  </div>

  <ul class="contacts">
    <li>
      <svg viewBox="0 0 10 10"><path d="M2 0.5 L3.5 0.5 L4 3 L3 3.8 C3.5 5 4.6 6.3 6 7 L6.8 6 L9.3 6.5 L9.3 8 C9.3 8.8 8.6 9.5 7.8 9.4 C4.2 9 1 5.8 0.6 2.2 C0.5 1.2 1.2 0.5 2 0.5 Z" fill="var(--white)"/></svg>
      0203 555 0178
    </li>
    <li>
      <svg viewBox="0 0 10 10"><rect x="0.7" y="2" width="8.6" height="6" fill="none" stroke="var(--white)" stroke-width="1"/><path d="M0.7 2 L5 5.5 L9.3 2" fill="none" stroke="var(--white)" stroke-width="1"/></svg>
      info@veltrona.com
    </li>
    <li>
      <svg viewBox="0 0 10 10"><circle cx="5" cy="5" r="4.3" fill="none" stroke="var(--white)" stroke-width="0.9"/><ellipse cx="5" cy="5" rx="1.9" ry="4.3" fill="none" stroke="var(--white)" stroke-width="0.8"/><path d="M0.7 5 H9.3 M1.5 3 H8.5 M1.5 7 H8.5" stroke="var(--white)" stroke-width="0.7"/></svg>
      www.veltrona.com
    </li>
  </ul>

  <address class="address">
    1287 Alder Street<br>
    Springfield, PA 15990
  </address>
</section>

</body>
</html>
```